Studying Effectively To Do List

I am looking to design a new "Study To Do List" for High School students (Ages 15 - 18) . This will be printed as an A4 notepad and so should only be a single A4 page.

The Design will need to be professional and look semi-serious but also be appealing to High school students (Ages 15 - 18) and should NOT be gender specific.

I have attached a word document outlining the structure of the page. The space provided should be large enough that people can write in it comfortably.

The notepad will most likely be printed in black and white but I'm also looking at coloured options - colours should be kept to a minimum.

This will be printed professionally and should also include a 3mm bleed.

The design should also include the business logo (included in the word document)

Target Market(s)

High School students (Ages 15 - 18). Both genders

Industry/Entity Type

Education

Font styles to use
Serif
Sans Serif

Requirements
Must have
• Please see the word document attached.
Should not have
• Too much colour

```html
<!DOCTYPE html>
<html lang="en">
<head>
<meta charset="utf-8">
<title>Studying Effectively To Do List</title>
<link href="https://fonts.googleapis.com/css2?family=Roboto+Condensed:wght@300;400;700&display=swap" rel="stylesheet">
<style>
  :root {
    --navy: #22354d;
    --orange: #f47721;
    --band: #dcdce1;
    --band-dark: #cfcfd5;
    --ink: #1f2a38;
    --soft: #5f6670;
    --rule: #4c5868;
    --backdrop: #e9e9ec;
    --paper: #ffffff;
  }
  * { margin: 0; padding: 0; box-sizing: border-box; }
  html, body { width: 1200px; height: 1200px; overflow: hidden; background: var(--backdrop); }
  body { font-family: "Roboto Condensed", "Arial Narrow", sans-serif; position: relative; }

  .sheet {
    position: absolute; left: 150px; top: 18px;
    width: 1000px; height: 1293px;
    background: var(--paper);
    transform: scale(0.9); transform-origin: 0 0;
    box-shadow: 0 4px 18px rgba(0,0,0,.15);
  }
  .sheet > * { position: absolute; }

  .bar-navy { background: var(--navy); }
  .bar-orange { background: var(--orange); }

  .brand { left: 62px; top: 60px; width: 180px; display: flex; align-items: center; gap: 10px;
    font-weight: 700; font-size: 30px; color: var(--navy); letter-spacing: .5px; }
  .brand-dot { width: 24px; height: 24px; border-radius: 50%; background: var(--orange); flex: none; }

  .title { left: 256px; top: 28px; font-size: 47px; font-weight: 700; color: var(--navy); white-space: nowrap; letter-spacing: -.3px; }
  .title .accent { color: var(--orange); }
  .label-lg { font-size: 25px; font-weight: 700; color: var(--navy); }

  .section-band { height: 29px; background: var(--band); }
  .section-title { font-size: 31px; font-weight: 700; color: var(--navy); line-height: 1; }

  .field { border-bottom: 1.5px solid var(--rule); height: 30px; font-size: 17px; color: var(--soft);
    display: flex; align-items: flex-end; padding: 0 0 1px 4px; white-space: nowrap; gap: 12px; }
  .field .num { color: var(--ink); }
  .field .key { color: var(--ink); font-size: 18px; width: 112px; flex: none; }
  .field sup { font-size: 9px; }
  .head { color: var(--ink); font-size: 18px; }
</style>
</head>
<body>
<main class="sheet">
  <div class="bar-navy" style="left:0;top:0;width:43px;height:20px"></div>
  <div class="bar-navy" style="left:254px;top:0;width:746px;height:18px"></div>
  <div class="bar-orange" style="left:0;top:139px;width:43px;height:23px"></div>
  <div class="bar-orange" style="left:254px;top:137px;width:746px;height:25px"></div>

  <div class="brand" style="top:92px"><span class="brand-dot"></span>Brightpath</div>

  <h1 class="title">STUDYING EFFECTIVELY <span class="accent">TO DO LIST</span></h1>
  <div class="label-lg" style="left:258px;top:96px">NAME</div>
  <div class="label-lg" style="left:718px;top:99px">DATE</div>

  <!-- Revision -->
  <div class="section-band" style="left:31px;top:207px;width:942px"></div>
  <h2 class="section-title" style="left:41px;top:209px">REVISION</h2>
  <div class="field" style="left:37px;top:241px;width:299px"><span class="num">1.</span>MATHS</div>
  <div class="field" style="left:37px;top:278px;width:299px"><span class="num">2.</span>EINGLISH</div>
  <div class="field" style="left:37px;top:312px;width:299px"><span class="num">3.</span>HISTORY</div>
  <div class="field" style="left:352px;top:241px;width:336px"><span class="num">4.</span>MATHS</div>
  <div class="field" style="left:352px;top:278px;width:336px"><span class="num">5.</span>EINGLISH</div>
  <div class="field" style="left:352px;top:312px;width:336px"><span class="num">6.</span>HISTORY</div>
  <div class="field" style="left:705px;top:241px;width:268px"><span class="num">7.</span>MATHS</div>
  <div class="field" style="left:705px;top:278px;width:268px"><span class="num">8.</span>EINGLISH</div>
  <div class="field" style="left:705px;top:312px;width:268px"><span class="num">9.</span>HISTORY</div>

  <!-- Homework -->
  <div class="section-band" style="left:35px;top:386px;width:938px"></div>
  <h2 class="section-title" style="left:45px;top:388px">HOMEWORK</h2>
  <div class="field head" style="left:37px;top:423px;width:298px">SUBJECT</div>
  <div class="field head" style="left:352px;top:423px;width:621px">TASK</div>
  <div class="field" style="left:37px;top:460px;width:298px">MATHS</div>
  <div class="field" style="left:37px;top:494px;width:298px">EINGLISH</div>
  <div class="field" style="left:37px;top:529px;width:298px">HISTORY</div>
  <div class="field" style="left:37px;top:566px;width:298px">SOCIAL SIC</div>
  <div class="field" style="left:37px;top:600px;width:298px"></div>
  <div class="field" style="left:37px;top:634px;width:298px"></div>
  <div class="field" style="left:37px;top:670px;width:298px"></div>
  <div class="field" style="left:37px;top:705px;width:298px"></div>
  <div class="field" style="left:352px;top:460px;width:621px">HOME WORK LESSONE NO 1 TO 5</div>
  <div class="field" style="left:352px;top:494px;width:621px">HOME WORK LESSONE NO 1 TO 5</div>
  <div class="field" style="left:352px;top:529px;width:621px">HOME WORK LESSONE NO 1 TO 5</div>
  <div class="field" style="left:352px;top:566px;width:621px">HOME WORK LESSONE NO 1 TO 5</div>
  <div class="field" style="left:352px;top:600px;width:621px"></div>
  <div class="field" style="left:352px;top:634px;width:621px"></div>
  <div class="field" style="left:352px;top:670px;width:621px"></div>
  <div class="field" style="left:352px;top:705px;width:621px"></div>

  <!-- Assessments -->
  <div class="section-band" style="left:34px;top:773px;width:939px"></div>
  <h2 class="section-title" style="left:45px;top:775px">ASSESSMENTS</h2>

  <div class="field" style="left:37px;top:808px;width:535px"><span class="key">ASSESSMENT</span>MATHS,&nbsp; EINGLISH, HISTORY</div>
  <div class="field" style="left:595px;top:808px;width:378px"><span class="key" style="width:35px">DUE</span>15<sup>TH</sup> JUNE 2017</div>
  <div class="field" style="left:37px;top:845px;width:936px"><span class="key">ELEMENT</span>NOOTBOOK OTHER ELEMENTS USING</div>

  <div class="field" style="left:37px;top:880px;width:535px"><span class="key">ASSESSMENT</span>MATHS,&nbsp; EINGLISH, HISTORY</div>
  <div class="field" style="left:595px;top:880px;width:378px"><span class="key" style="width:35px">DUE</span>15<sup>TH</sup> JUNE 2017</div>
  <div class="field" style="left:37px;top:913px;width:936px"><span class="key">ELEMENT</span></div>

  <div class="field" style="left:37px;top:950px;width:535px"><span class="key">ASSESSMENT</span>MATHS,&nbsp; EINGLISH, HISTORY</div>
  <div class="field" style="left:595px;top:950px;width:378px"><span class="key" style="width:35px">DUE</span>15<sup>TH</sup> JUNE 2017</div>
  <div class="field" style="left:37px;top:985px;width:936px"><span class="key">ELEMENT</span></div>

  <div class="field" style="left:37px;top:1019px;width:535px"><span class="key">ASSESSMENT</span>MATHS,&nbsp; EINGLISH, HISTORY</div>
  <div class="field" style="left:595px;top:1019px;width:378px"><span class="key" style="width:68px">DUE</span>JUNE 2017</div>
  <div class="field" style="left:37px;top:1054px;width:936px"><span class="key">ELEMENT</span></div>

  <!-- Notes & Practice -->
  <div class="section-band" style="left:34px;top:1112px;width:538px"></div>
  <div style="left:34px;top:1112px;width:102px;height:29px;background:var(--band-dark)"></div>
  <h2 class="section-title" style="left:44px;top:1116px;font-size:26px">NOTES</h2>
  <div class="section-band" style="left:586px;top:1112px;width:387px"></div>
  <h2 class="section-title" style="left:596px;top:1115px;font-size:26px">PRACTICE</h2>

  <div class="field" style="left:37px;top:1149px;width:275px"><span class="num">1.</span>NOOTBOOK OTHER</div>
  <div class="field" style="left:37px;top:1183px;width:275px"><span class="num">2.</span></div>
  <div class="field" style="left:37px;top:1219px;width:275px"><span class="num">3.</span></div>
  <div class="field" style="left:324px;top:1149px;width:248px"><span class="num">4.</span></div>
  <div class="field" style="left:324px;top:1183px;width:248px"><span class="num">5.</span></div>
  <div class="field" style="left:324px;top:1219px;width:248px"><span class="num">6.</span></div>
  <div class="field" style="left:595px;top:1149px;width:378px">MATHS,&nbsp; EINGLISH, HISTORY</div>
  <div class="field" style="left:595px;top:1183px;width:378px"></div>
  <div class="field" style="left:595px;top:1219px;width:378px"></div>
</main>
</body>
</html>
```